Ridgeway Business Card Redesign

Using the current logo/tagline lock-up and icon, redesign the Ridgeway business card to better show the tagline and improve the layout to give the card a more timely design and a classic, sophisticated look. See attached Project Brief for more detail.

```html
<!DOCTYPE html>
<html lang="en">
<head>
<meta charset="utf-8">
<title>Ridgeway Capital Business Card</title>
<link href="https://fonts.googleapis.com/css2?family=Cinzel:wght@400;600&family=Open+Sans:wght@400;600&display=swap" rel="stylesheet">
<style>
  :root {
    --backdrop: #9b9b9b;
    --card: #ffffff;
    --ink: #3c3c3e;
    --blue: #1a78c2;
    --band: #3d3d3f;
    --rule: #cfcfcf;
  }
  html, body { margin: 0; padding: 0; }
  body {
    width: 1133px; height: 1200px; overflow: hidden;
    background: var(--backdrop);
    position: relative;
    font-family: "Open Sans", Arial, sans-serif;
  }
  .card {
    position: absolute; left: 215px; width: 701px; height: 402px;
    background: var(--card); overflow: hidden;
  }
  .card--front { top: 148px; }
  .card--back { top: 647px; }

  .spread { display: flex; justify-content: space-between; line-height: 1; }

  /* Front */
  .front-name {
    position: absolute; left: 120px; top: 116px; width: 461px;
    color: var(--ink); font-family: "Cinzel", Georgia, serif; font-weight: 400;
  }
  .front-name__main { font-size: 80px; }
  .front-name__sub { font-size: 38px; margin-top: 6px; }
  .front-rule {
    position: absolute; left: 120px; top: 236px; width: 461px; height: 2px;
    background: var(--ink);
  }
  .front-tagline {
    position: absolute; left: 120px; top: 246px; width: 464px;
    color: var(--blue); font-family: "Cinzel", Georgia, serif; font-weight: 600;
    font-size: 25px; letter-spacing: 2.6px; white-space: nowrap;
  }

  /* Back */
  .brand { position: absolute; left: 38px; top: 145px; display: flex; align-items: center; }
  .brand__dot { width: 76px; height: 76px; border-radius: 50%; background: var(--blue); margin-right: 16px; }
  .brand__name { color: var(--ink); font-family: "Cinzel", Georgia, serif; font-weight: 400; width: 210px; }
  .brand__main { font-size: 37px; }
  .brand__sub { font-size: 16px; margin-top: 4px; }

  .divider { position: absolute; left: 368px; top: 72px; width: 1px; height: 230px; background: var(--rule); }

  .contact { position: absolute; left: 394px; top: 72px; color: var(--ink); }
  .contact__name {
    margin: 0; color: var(--blue); font-family: "Cinzel", Georgia, serif; font-weight: 600;
    font-size: 25px; line-height: 1; letter-spacing: 0.5px;
  }
  .contact__title { margin: 5px 0 0; font-size: 15px; }
  .contact__address { margin: 18px 0 0; font-size: 15px; line-height: 22px; font-style: normal; }
  .contact__list { margin: 14px 0 0; padding: 0; list-style: none; font-size: 15px; }
  .contact__list li { display: flex; height: 26px; align-items: center; }
  .contact__label { width: 54px; color: var(--blue); font-weight: 600; }

  .footer-art { position: absolute; left: 0; bottom: 0; }
  .footer-tagline {
    position: absolute; left: 390px; right: 22px; bottom: 8px; color: #fff;
    font-weight: 600; font-size: 17px; letter-spacing: 0.3px; text-align: right; white-space: nowrap;
  }
</style>
</head>
<body>
  <section class="card card--front">
    <div class="front-name">
      <div class="spread front-name__main"><span>R</span><span>I</span><span>D</span><span>G</span><span>E</span><span>W</span><span>A</span><span>Y</span></div>
      <div class="spread front-name__sub"><span>C</span><span>A</span><span>P</span><span>I</span><span>T</span><span>A</span><span>L</span></div>
    </div>
    <div class="front-rule"></div>
    <div class="front-tagline">Partner-Led Growth Equity</div>
  </section>

  <section class="card card--back">
    <div class="brand">
      <div class="brand__dot"></div>
      <div class="brand__name">
        <div class="spread brand__main"><span>R</span><span>I</span><span>D</span><span>G</span><span>E</span><span>W</span><span>A</span><span>Y</span></div>
        <div class="spread brand__sub"><span>C</span><span>A</span><span>P</span><span>I</span><span>T</span><span>A</span><span>L</span></div>
      </div>
    </div>

    <div class="divider"></div>

    <div class="contact">
      <h1 class="contact__name">Daniel R. Whitfield</h1>
      <p class="contact__title">Principal &amp; Chief Marketing Officer</p>
      <address class="contact__address">47 Harbor Mill Road Suite 210<br>Milford, CT 06460</address>
      <ul class="contact__list">
        <li><span class="contact__label">Direct:</span>(555) 201-4837</li>
        <li><span class="contact__label">Cell:</span>(555) 318-6620</li>
        <li><span class="contact__label">Email:</span>dwhitfield@ridgewaycapital.com</li>
        <li><span class="contact__label">Web:</span>www.ridgewaycapital.com</li>
      </ul>
    </div>

    <svg class="footer-art" width="701" height="40" viewBox="0 0 701 40" aria-hidden="true">
      <polygon points="0,22 335,22 318,40 0,40" fill="var(--blue)"/>
      <polygon points="378,4 701,4 701,40 334,40" fill="var(--band)"/>
    </svg>
    <div class="footer-tagline">PARTNER-LED GROWTH EQUITY</div>
  </section>
</body>
</html>
```